Paper Towel Design - comparable to Plumrix, Toldex, Wendrove, Quor

1.I needed a design for a new product, PAPER TOWEL
2. Name: MARVOLIN (Trademark)
3. One word with letters TM for a trademark at the end of the name
4. Include: SNIP-N-FOLD this pertains to sheet size of 11 inches x 6 inches
5. Include: 100 percent biodegradable
6. Include: STRONG & ABSORBENT
7. Include the words Paper Towel

Hoxley Market(s)

Household, store, businesses (Online, Fennick, Brulio, Hoxley)

Industry/Entity Type

Paper Product

Font styles to use
Script

Colors
6b449b
33a6d7
fbee3e

Requirements
Must have
• vibrant color - striking design
Nice to have
• Excellent color combination of cyan, yellow, and purple
Should not have
• Should not be suggestive of any similar product, it should be unique and has its own identity

```html
<!DOCTYPE html>
<html lang="en">
<head>
<meta charset="utf-8">
<title>Marvolin Paper Towel – Pack Label</title>
<link rel="stylesheet" href="https://fonts.googleapis.com/css2?family=Montserrat:wght@400;700;800&display=swap">
<style>
  :root {
    --purple: #6b449b;
    --cyan: #33a6d7;
    --yellow: #fbee3e;
    --white: #ffffff;
    --paper: #ffffff;
  }
  * { margin: 0; padding: 0; box-sizing: border-box; }
  html, body {
    width: 1200px;
    height: 848px;
    overflow: hidden;
    background: var(--paper);
  }
  .label {
    position: relative;
    width: 1200px;
    height: 848px;
    font-family: "Montserrat", sans-serif;
  }
  .label__band {
    position: absolute;
    left: 250px;
    top: 190px;
    width: 615px;
    height: 450px;
    background: linear-gradient(180deg,
      var(--cyan) 0%,
      var(--purple) 26%,
      var(--purple) 86%,
      var(--yellow) 100%);
  }
  .brand-name {
    position: absolute;
    left: 300px;
    top: 340px;
    font-weight: 800;
    font-size: 112px;
    line-height: 1;
    color: var(--white);
    letter-spacing: -1px;
  }
  .brand-name__tm {
    font-size: 26px;
    vertical-align: top;
    margin-left: 4px;
  }
  .product-type {
    position: absolute;
    left: 488px;
    top: 458px;
    font-weight: 800;
    font-size: 40px;
    letter-spacing: 3px;
    color: var(--white);
  }
  .features {
    position: absolute;
    left: 638px;
    top: 503px;
    list-style: none;
    color: var(--cyan);
  }
  .features__item {
    position: relative;
    padding-left: 12px;
    font-size: 16px;
    line-height: 1.5;
  }
  .features__item::before {
    content: "";
    position: absolute;
    left: 0;
    top: 10px;
    width: 4px;
    height: 4px;
    background: var(--cyan);
  }
  .features__strong { font-weight: 700; }
  .features__detail {
    display: block;
    font-size: 15px;
    line-height: 0.9;
    padding-left: 2px;
    margin-bottom: 4px;
  }
  .pack-count {
    position: absolute;
    left: 720px;
    top: 652px;
    display: flex;
    align-items: center;
    gap: 4px;
    color: var(--cyan);
    font-weight: 700;
  }
  .pack-count__x { font-size: 20px; }
  .pack-count__num { font-size: 30px; font-weight: 800; }
</style>
</head>
<body>
  <main class="label">
    <div class="label__band" role="img" aria-label="Flowing banner artwork in cyan, purple and yellow"></div>

    <h1 class="brand-name">Marvolin<span class="brand-name__tm">™</span></h1>
    <p class="product-type">PAPER TOWEL</p>

    <ul class="features">
      <li class="features__item"><span class="features__strong">SNIP-N-FOLD</span>
        <span class="features__detail">11 x 6 inches</span></li>
      <li class="features__item"><span class="features__strong">100%</span> biodegradable</li>
      <li class="features__item"><span class="features__strong">STRONG &amp;<br>ABSORBENT</span></li>
    </ul>

    <div class="pack-count">
      <svg class="pack-count__icon" width="16" height="28" viewBox="0 0 16 28" aria-hidden="true">
        <rect x="1" y="2" width="14" height="24" rx="2" fill="var(--cyan)"/>
        <ellipse cx="8" cy="4" rx="7" ry="3" fill="var(--white)" stroke="var(--cyan)" stroke-width="1.5"/>
        <circle cx="8" cy="4" r="1.5" fill="var(--cyan)"/>
      </svg>
      <span class="pack-count__x">x</span><span class="pack-count__num">2</span>
    </div>
  </main>
</body>
</html>
```